Website for New Medical Professional Organization Anti-Aging

Thanks to all who participated in my logo design project! We had several very good options to choose from, but we decided to go with the project attached by Remko.

Now, we need to develop the same idea into a web page. Our membership will be professionals involved in anti-aging medicine including doctors, naturopaths, chiropractors, nurses, nurse practioners, etc and also the corporations that have an interest eg. testing facilities, pharmacies, etc.

The sections will be :\
About Us
Membership
Certification
Conferences
Directory
Classifieds
Community

We need at least 2 areas for pictures that change content. One large one smaller.

1. Banner for the top, which includes the Logo, social media contacts, phone number, website address www.vlorbex.ca. We are thinking of using the black backround for the banner, then white backround with black and gold headings for the body.

2. Banner for footer: black again with small logo and contact information

3. The corporate sponsor banner can go across the bottom just above the footer banner. This one can be moving right to left to reveal the corporate sponsor names.

We need a section for "Join Now" where they are lead to a place to enter name, profession, address, email, phone, etc.

We need a nice looking "cart" for purchases on the webpage...

Our competition (and leader in the field is www.q7tz.com. We like some of their ideas, but it looks disorganized and too commercial. We want to look professional but friendly and interesting.
Updates

I am hoping that you all can "see" the logo on the black backround ... I can't see it on mine because I don't have editing software... I really like the gold logo on black as the designer provided.

Thanks and good luck!

I chose a gold colour from the colour wheel, but what I really want is for the logo colour to be present in the website design and become a prominent part of the design. Thanks for your work so far!

Marla

Hello designers!

I really like the ones that have more black in them. I would like to see more use of the Logo - make it bigger and a more integral pat of the website design. Since we are Canadian, we probably should have some red somewhere too :) So, now I am thinking Gold, Black, White and Red. I am not liking the silver I have seen so far. Please try to make the gold more regal and glowing. Thanks!

Marla

Target Market(s)

professionals - doctors, chiropractors, naturopaths, nurses
commercial health providers - pharmacy, testing facilities, etc

Industry/Entity Type

Nurse

Colors
ffcf3e
000000
d5d5d5

Requirements
Must have
• social media
contact info
e commerce

```html
<!DOCTYPE html>
<html lang="en">
<head>
<meta charset="utf-8">
<title>Vlorbex Society of Renewal Medicine</title>
<link rel="stylesheet" href="https://fonts.googleapis.com/css2?family=Cinzel:wght@600&family=Sorts+Mill+Goudy:ital@0;1&family=Open+Sans:wght@300;400&display=swap">
<style>
:root{
  --gold:#b08a3e;
  --gold-light:#c9a24e;
  --black:#000;
  --band:#111;
  --red:#f00;
  --white:#fff;
  --text:#444;
  --grey:#d5d5d5;
}
*{box-sizing:border-box;margin:0;padding:0}
html,body{width:1090px;height:1200px;overflow:hidden}
body{position:relative;background:var(--white);font-family:"Open Sans",sans-serif;color:var(--text)}
.abs{position:absolute}
.serif{font-family:"Sorts Mill Goudy",serif}

.site-header{left:0;top:0;width:1090px;height:617px;background:radial-gradient(ellipse at 50% 40%,#1c1c1c 0%,#000 70%)}
.gold-rule{left:0;width:1090px;height:5px;background:var(--gold)}
.member-bar{left:796px;top:5px;width:151px;height:20px;background:var(--gold);color:var(--white);font:11px "Sorts Mill Goudy",serif;display:flex;align-items:center;justify-content:center;gap:5px}
.brand{left:143px;top:20px;display:flex;align-items:center;gap:12px}
.brand-mark{width:72px;height:72px;background:var(--gold)}
.brand-name{font-family:"Cinzel",serif;font-weight:600;color:var(--gold-light);font-size:23px;line-height:25px;border-left:2px solid var(--gold);padding-left:8px}
.social{right:143px;top:54px;display:flex;gap:10px}
.social span{display:flex;align-items:center;gap:4px;color:var(--grey);font-size:11px}
.social i{display:block;width:12px;height:12px;border-radius:50%;background:var(--gold)}
.call{right:143px;top:80px;font:23px "Sorts Mill Goudy",serif;color:var(--gold)}
.nav{left:143px;top:124px;width:804px;height:25px;border-top:1px solid var(--gold);border-bottom:1px solid var(--gold);display:flex;justify-content:space-between;align-items:center}
.nav a{font:13.5px "Sorts Mill Goudy",serif;color:var(--grey);text-decoration:none;padding:0 10px;height:23px;line-height:23px}
.nav a.active{background:var(--red);color:var(--white)}
.hero{left:143px;top:163px;width:804px;height:335px;background:linear-gradient(180deg,#b9c8d8 0%,#8e9aa6 40%,#6c6f73 75%,#a8764a 100%)}
.hero-panel{left:161px;top:178px;width:309px;height:305px;background:rgba(230,230,230,.88);text-align:center;color:#111}
.hero-panel .t1{margin-top:30px;font-size:26px;line-height:25px}
.hero-panel .t2{font-size:44px;color:var(--gold);line-height:46px}
.hero-panel .quote{font-style:italic;font-size:25px;line-height:30px;margin-top:6px;position:relative}
.hero-panel .quote b{position:absolute;font-size:70px;color:#777;font-style:normal;line-height:1}
.hero-panel .date{font-size:13.5px;margin-top:24px}
.dots{left:521px;top:469px;display:flex;gap:8px}
.dots i{width:10px;height:10px;border-radius:50%;background:var(--white)}
.dots i.on{background:var(--red)}
.join-band{left:0;top:505px;width:1090px;height:112px;background:var(--band)}
.join-title{right:390px;top:535px;font:29px "Sorts Mill Goudy",serif;color:var(--gold);text-align:right}
.join-sub{right:390px;top:574px;font-size:13.4px;font-weight:300;color:#ddd}
.join-btn{left:737px;top:542px;width:210px;height:53px;background:var(--red);color:var(--white);font:23px "Sorts Mill Goudy",serif;display:flex;align-items:center;justify-content:center}

.sec-title{color:var(--gold);font-family:"Sorts Mill Goudy",serif}
.side-photo{left:143px;top:688px;width:327px;height:229px;background:linear-gradient(180deg,#c9ccce 0%,#707478 45%,#3d4349 80%,#8f949a 100%)}
.mini-arrows{left:433px;top:659px;display:flex;gap:2px}
.mini-arrows span{width:17px;height:17px;background:var(--red);display:flex;align-items:center;justify-content:center}
.welcome p{font-size:13.4px;font-weight:300;line-height:21px;color:#444;margin-bottom:8px}
.sponsors{left:170px;top:1008px;width:750px;display:flex;justify-content:space-around;align-items:center}
.sponsor{display:flex;align-items:center;gap:6px;font:24px "Sorts Mill Goudy",serif;color:#333}
.sponsor i{width:22px;height:22px;border-radius:50%;background:#333}

.footer{left:0;top:1090px;width:1090px;height:104px;background:var(--black);color:#ddd;font-size:11px}
.foot-h{font:13px "Sorts Mill Goudy",serif;color:var(--gold);text-transform:uppercase}
.foot-col{line-height:17px}
</style>
</head>
<body>
<header class="abs site-header"></header>
<div class="abs gold-rule" style="top:0"></div>
<div class="abs member-bar">Members Log-in | Cart
  <svg width="14" height="12" viewBox="0 0 14 12"><path d="M0 1h3l2 7h7l2-5H4" fill="none" stroke="#fff" stroke-width="1.4"/><circle cx="6" cy="10.5" r="1.2" fill="#fff"/><circle cx="11" cy="10.5" r="1.2" fill="#fff"/></svg>
</div>
<div class="abs brand"><span class="brand-mark"></span><span class="brand-name">Vlorbex Society<br>of Renewal Medicine</span></div>
<div class="abs social"><span><i></i>Gleam</span><span><i></i>Folio</span><span><i></i>Tweeko</span></div>
<div class="abs call">call now: 012-345-7890</div>
<nav class="abs nav">
  <a>Home</a><a>About Us</a><a class="active">Membership</a><a>Certification</a><a>Conferences</a><a>Directory</a><a>Classifieds</a><a>Community</a><a>Contact</a>
</nav>

<div class="abs hero" role="img" aria-label="Autumn aerial view of Montreal skyline"></div>
<div class="abs hero-panel serif">
  <div class="t1">Vlorbex Society of<br>Renewal Medicine</div>
  <div class="t2">Symposium</div>
  <div class="quote"><b style="left:20px;top:-6px">“</b>Applying Functional<br>Medicine to Restore<br>Patient Health<b style="right:28px;top:50px">”</b></div>
  <div class="date">October 20, 2014 &nbsp;|&nbsp; Montreal, Canada</div>
</div>
<div class="abs dots"><i></i><i class="on"></i><i></i></div>
<svg class="abs" style="left:104px;top:324px" width="24" height="44" viewBox="0 0 24 44"><path d="M20 2L3 22l17 20" fill="none" stroke="#f00" stroke-width="2"/></svg>
<svg class="abs" style="left:962px;top:324px" width="24" height="44" viewBox="0 0 24 44"><path d="M4 2l17 20L4 42" fill="none" stroke="#f00" stroke-width="2"/></svg>

<section class="abs join-band"></section>
<h2 class="abs join-title" style="font-weight:400">Header Text with Join Now Button</h2>
<p class="abs join-sub">Some sub text ut perspiciatis unde omnis iste natus error sit voluptatem each quesa lorem it.</p>
<div class="abs join-btn">JOIN NOW</div>

<h3 class="abs sec-title" style="left:143px;top:651px;font-size:24px;font-weight:400">Second Picture (Smaller)</h3>
<div class="abs mini-arrows">
  <span><svg width="8" height="12"><path d="M7 1L2 6l5 5" fill="none" stroke="#fff" stroke-width="1.4"/></svg></span>
  <span><svg width="8" height="12"><path d="M1 1l5 5-5 5" fill="none" stroke="#fff" stroke-width="1.4"/></svg></span>
</div>
<div class="abs side-photo" role="img" aria-label="Seated conference attendees in business attire"></div>

<section class="abs welcome" style="left:510px;top:655px;width:450px">
  <h1 class="sec-title" style="font-size:30px;font-weight:400;line-height:38px;margin-bottom:18px">Welcome to Vlorbex<br>Society of Renewal Medicine</h1>
  <p>Sed ut perspiciatis unde omnis iste natus error sit voluptatem each que sa quae ab illo inventore veritatis et quasi architecto bea tae vitae dicta sunt explicabo. Nemo enim ipsam voluptatem quia volup tas sit aspernatur aut odit aut fugit. Essed quia consequuntur magni doluptatem sequi nesciunt Neque porro quisquam est, qui dolorem ipsum quia.</p>
  <p>Tus modi tempora incidunt ut labore et dolore magnam aliquam quaerat voluptatem. Ut enim ad minima veniam, quis nostrum exercitationem ul lam corporis suscipit laborios.</p>
</section>

<h3 class="abs sec-title" style="left:0;width:1090px;top:962px;text-align:center;font-size:20px;font-weight:400">VSRM Sponsors</h3>
<svg class="abs" style="left:140px;top:1018px" width="14" height="26" viewBox="0 0 14 26"><path d="M12 1L2 13l10 12" fill="none" stroke="#f00" stroke-width="1.6"/></svg>
<svg class="abs" style="left:934px;top:1018px" width="14" height="26" viewBox="0 0 14 26"><path d="M2 1l10 12L2 25" fill="none" stroke="#f00" stroke-width="1.6"/></svg>
<div class="abs sponsors">
  <span class="sponsor"><i></i>Quellon Lab</span>
  <span class="sponsor"><i></i>Ardmix</span>
  <span class="sponsor">Tessaro Diagnostics</span>
  <span class="sponsor">Corvane MD</span>
</div>

<footer class="abs footer">
  <div class="abs" style="left:143px;top:18px">
    <div class="foot-h">Pages</div>
    <div style="display:flex;gap:22px" class="foot-col">
      <div>Home<br>About Us<br>Classifieds</div>
      <div>Membership<br>Certification<br>Community</div>
      <div>Conferences<br>Directory<br>FAQ</div>
    </div>
  </div>
  <div class="abs foot-col" style="left:425px;top:18px">
    <div class="foot-h">Contact Details</div>
    p: +123 456 7890 &nbsp;f: +123 456 7891<br>PO Box 123, Main City Address Here<br>My City and Country, 2331
  </div>
  <div class="abs" style="left:676px;top:22px;display:flex;align-items:center;gap:8px">
    <span style="width:44px;height:44px;background:var(--gold)"></span>
    <div>
      <div style="font:600 15px/16px Cinzel,serif;color:var(--gold-light);border-left:1px solid var(--gold);padding-left:5px">Vlorbex Society<br>of Renewal Medicine</div>
      <div style="margin-top:6px;font-size:10.5px">Copyright © VSRM 2014 All Rights Reserved</div>
    </div>
  </div>
</footer>
<div class="abs gold-rule" style="top:1194px;height:6px"></div>
</body>
</html>
```